Cedar Hall businesscard

We changed our name and logo, now we need new business cards.
3-4/72 Marlow Street Blacktown 2148
www.cedarhall-example.org.au
info@cedarhall-example.org.au
Lorna-Jean Whitcombe
Senior Pastor
ph: 02 95874210

```html
<!DOCTYPE html>
<html lang="en">
<head>
<meta charset="utf-8">
<title>Cedar Hall Business Card</title>
<link rel="stylesheet" href="https://fonts.googleapis.com/css2?family=Arimo:wght@400;700&display=swap">
<style>
  :root {
    --backdrop: #2a2b2d;
    --card-light: #f7f7f7;
    --card-mid: #e6e6e7;
    --slate: #5f6973;
    --slate-text: #6e7a86;
    --accent-red: #9b3027;
    --ink: #2d2d2d;
    --icon: #e9ecef;
  }
  html, body {
    margin: 0;
    padding: 0;
    width: 1200px;
    height: 1116px;
    overflow: hidden;
    background: var(--backdrop);
    font-family: "Arimo", Arial, sans-serif;
  }
  .business-card {
    position: absolute;
    left: 100px;
    top: 272px;
    width: 1000px;
    height: 572px;
    border-radius: 36px;
    overflow: hidden;
    box-shadow: 0 10px 30px rgba(0,0,0,0.45);
  }
  .card-art {
    position: absolute;
    inset: 0;
    width: 1000px;
    height: 572px;
  }
  .brand {
    position: absolute;
    left: 600px;
    top: 112px;
    display: flex;
    align-items: center;
    gap: 18px;
  }
  .brand-dot {
    width: 40px;
    height: 40px;
    border-radius: 50%;
    background: var(--slate);
  }
  .brand-name {
    font-size: 40px;
    font-weight: 400;
    letter-spacing: 2px;
    color: var(--slate);
    white-space: nowrap;
  }
  .holder {
    position: absolute;
    left: 52px;
    top: 168px;
  }
  .holder-name {
    font-size: 30px;
    color: var(--slate-text);
    margin: 0;
    font-weight: 400;
  }
  .holder-role {
    font-size: 15px;
    color: var(--ink);
    letter-spacing: 0.5px;
    margin: 4px 0 0;
  }
  .contact-list {
    position: absolute;
    left: 100px;
    top: 300px;
    margin: 0;
    padding: 0;
    list-style: none;
  }
  .contact-list li {
    height: 38px;
    line-height: 26px;
    font-size: 19px;
    color: var(--ink);
    white-space: nowrap;
  }
</style>
</head>
<body>
  <div class="business-card">
    <svg class="card-art" viewBox="0 0 1000 572" aria-hidden="true">
      <defs>
        <linearGradient id="card-face" x1="0" y1="0" x2="1" y2="1">
          <stop offset="0" stop-color="var(--card-light)"/>
          <stop offset="1" stop-color="var(--card-mid)"/>
        </linearGradient>
      </defs>
      <rect width="1000" height="572" fill="url(#card-face)"/>
      <path class="accent-stripe" d="M0,500 Q520,502 1000,330 L1000,350 Q525,520 0,518 Z" fill="var(--accent-red)"/>
      <path class="base-band" d="M0,518 Q525,520 1000,350 L1000,572 L0,572 Z" fill="var(--slate)"/>
      <rect class="icon-tab" x="-24" y="286" width="96" height="240" rx="20" fill="var(--slate)"/>
      <g class="contact-icons" fill="var(--icon)">
        <g class="icon-phone" transform="translate(0,-17)">
          <path d="M22,320 h26 a3,3 0 0 1 3,3 v3 h-8 v-3 h-16 v3 h-8 v-3 a3,3 0 0 1 3,-3 z M26,328 h18 l5,12 h-28 z"/>
        </g>
        <g class="icon-mail" transform="translate(0,-17)">
          <rect x="21" y="358" width="30" height="20" rx="2"/>
          <path d="M22,360 L36,371 L50,360" fill="none" stroke="var(--slate)" stroke-width="2.5"/>
        </g>
        <g class="icon-link" transform="translate(0,-21)" fill="none" stroke="var(--icon)" stroke-width="4" stroke-linecap="round">
          <path d="M30,412 l-4,4 a5,5 0 0 0 7,7 l4,-4"/>
          <path d="M42,408 l4,-4 a5,5 0 0 0 -7,-7 l-4,4"/>
          <path d="M32,414 l8,-8"/>
        </g>
        <g class="icon-pin" transform="translate(0,-24)">
          <path d="M36,436 a11,11 0 0 1 11,11 c0,8 -11,19 -11,19 c0,0 -11,-11 -11,-19 a11,11 0 0 1 11,-11 z"/>
          <circle cx="36" cy="447" r="4" fill="var(--slate)"/>
        </g>
      </g>
    </svg>

    <div class="brand">
      <span class="brand-dot"></span>
      <span class="brand-name">CEDAR HALL</span>
    </div>

    <div class="holder">
      <p class="holder-name">Lorna-Jean Whitcombe</p>
      <p class="holder-role">SENIOR PASTOR</p>
    </div>

    <ul class="contact-list">
      <li>02 95874210</li>
      <li>info@cedarhall-example.org.au</li>
      <li>www.cedarhall-example.org.au</li>
      <li>3-4/72 Marlow Street, Blacktown 2148</li>
    </ul>
  </div>
</body>
</html>
```